Redesign CanvoMira's Artist Profile Page

CanvoMira is a contemporary arts website that has a large worldwide community of artists with profile pages for each artist showing artwork, exhibits, bio data, etc.

For an example please see: http://www.canvomira-example.com/global/artists/show/40731-orin-haskel

We would like a slight redesign on these pages within the context of the current website. We are interested in modernizing and lightening the design. The artwork should be the primary focus.

Target Market(s)

Professional artists, galleries and collectors

Industry/Entity Type

Artists

Requirements
Must have
• All the current functionality on the page.

```html
<!DOCTYPE html>
<html lang="en">
<head>
<meta charset="utf-8">
<title>CanvoMira – Orin Haskel – Artist Profile</title>
<link rel="stylesheet" href="https://fonts.googleapis.com/css2?family=Questrial&family=Open+Sans:wght@400;600&family=Roboto+Condensed:wght@300;400&display=swap">
<style>
  :root {
    --olive: #7e7f0f;
    --panel-grey: #c6c6c6;
    --frame-grey: #a9a9a9;
    --ink: #111111;
    --ink-soft: #555555;
    --footer-grey: #9a9a9a;
    --page: #ffffff;
    --line: #a0a0a0;
  }
  * { box-sizing: border-box; margin: 0; padding: 0; }
  html, body { width: 1200px; height: 838px; overflow: hidden; background: var(--page); }
  body { position: relative; font-family: "Open Sans", Verdana, sans-serif; color: var(--ink); }
  .abs { position: absolute; }

  /* Utility bar */
  .utility-bar { left: 740px; top: 0; width: 260px; height: 20px; }
  .utility-bar svg { position: absolute; left: 0; top: 0; }
  .utility-links { position: absolute; left: 0; top: 0; width: 260px; height: 20px; display: flex; justify-content: center; align-items: center; gap: 17px; font-size: 11px; color: #fff; }

  /* Brand */
  .brand { left: 220px; top: 22px; font-family: "Questrial", sans-serif; font-size: 44px; color: var(--ink-soft); letter-spacing: -1px; line-height: 1; }

  /* Search */
  .search { left: 797px; top: 43px; width: 185px; height: 21px; border: 1px solid #c9c9c9; background: #fff; font-size: 12px; color: #8a8a8a; padding: 2px 9px; }
  .search-toggle { position: absolute; right: 2px; top: 2px; width: 15px; height: 15px; background: var(--olive); }
  .search-toggle svg { display: block; }

  /* Main sheet */
  .sheet { left: 200px; top: 81px; width: 800px; height: 685px; background: #fff; box-shadow: 0 0 6px rgba(0,0,0,0.35); }

  .main-nav { left: 220px; top: 81px; height: 62px; font-family: "Questrial", sans-serif; font-size: 16.5px; letter-spacing: -0.2px; }
  .main-nav a { position: absolute; top: 0; height: 62px; padding-top: 14px; color: var(--ink); text-decoration: none; white-space: nowrap; }
  .main-nav a.is-active { background: var(--olive); width: 75px; text-align: center; }

  .artist-name { left: 222px; top: 166px; font-family: "Questrial", sans-serif; font-size: 18px; font-weight: 400; }

  .profile-tabs a { position: absolute; top: 198px; width: 78px; height: 34px; background: var(--olive); font-size: 11px; color: var(--ink); text-decoration: none; text-align: center; line-height: 34px; }
  .profile-tabs a.is-active { background: var(--panel-grey); }

  .profile-panel { left: 220px; top: 232px; width: 762px; height: 364px; background: var(--panel-grey); }

  .feature-frame { left: 237px; top: 248px; width: 401px; height: 266px; background: var(--frame-grey); padding: 4px; }
  .feature-image { width: 100%; height: 100%; background: linear-gradient(180deg, #9fbbe0 0%, #c9d2da 22%, #8d8e92 42%, #a9a39b 62%, #7b6f64 82%, #8f8578 100%); }

  .thumb-strip { left: 237px; top: 524px; width: 401px; height: 56px; }
  .thumb-arrow { position: absolute; top: 0; width: 18px; height: 56px; background: var(--frame-grey); }
  .thumb-arrow svg { position: absolute; left: 5px; top: 22px; }
  .thumb { position: absolute; top: 0; width: 56px; height: 56px; background: var(--frame-grey); padding: 4px; }
  .thumb span { display: block; width: 100%; height: 100%; }

  .buzz-title { left: 654px; top: 249px; font-family: "Questrial", sans-serif; font-size: 13px; font-weight: 400; }
  .buzz-item { left: 654px; font-size: 9.5px; }

  .panel-divider { left: 861px; top: 252px; width: 1px; height: 258px; background: var(--line); }
  .avatar { left: 880px; top: 248px; width: 88px; height: 87px; background: linear-gradient(180deg, #d7dbe3 0%, #9aa9c6 55%, #3d5a96 100%); }
  .avatar-caption { left: 864px; top: 342px; width: 120px; text-align: center; font-size: 9.5px; }

  .quick-facts { left: 230px; top: 617px; }
  .quick-facts h2 { font-family: "Questrial", sans-serif; font-weight: 400; font-size: 13.5px; margin-bottom: 5px; }
  .quick-facts dl { font-size: 10px; display: grid; grid-template-columns: 70px auto; row-gap: 6px; line-height: 14px; }
  .quick-facts dd::before { content: ":  "; white-space: pre; }

  .statement { left: 354px; top: 608px; width: 628px; height: 105px; background: var(--panel-grey); padding: 11px 15px; }
  .statement h2 { font-weight: 400; font-size: 10px; margin-bottom: 4px; }
  .statement p { font-size: 10.3px; line-height: 20px; }

  .share-row { left: 763px; top: 731px; display: flex; gap: 4px; }
  .share-row span { width: 18px; height: 18px; border-radius: 3px; }

  .site-footer { left: 0; top: 782px; width: 1200px; font-family: "Roboto Condensed", sans-serif; }
  .footer-links a { position: absolute; top: 0; font-size: 11.5px; font-weight: 300; color: var(--footer-grey); text-decoration: none; }
  .copyright { position: absolute; left: 0; top: 28px; width: 1174px; text-align: center; font-family: "Open Sans", sans-serif; font-size: 9px; color: var(--ink-soft); }
</style>
</head>
<body>

  <div class="abs utility-bar">
    <svg width="260" height="20" viewBox="0 0 260 20" aria-hidden="true"><polygon points="0,0 260,0 240,20 20,20" fill="var(--olive)"/></svg>
    <nav class="utility-links"><span>Register Free</span><span>|</span><span>Sign In</span><span>|</span><span>FAQ</span></nav>
  </div>

  <div class="abs brand">CanvoMira</div>

  <div class="abs search">Search Worldwide
    <span class="search-toggle"><svg width="15" height="15" viewBox="0 0 15 15" aria-hidden="true"><polygon points="4,6 11,6 7.5,10" fill="#fff"/></svg></span>
  </div>

  <div class="abs sheet"></div>

  <nav class="abs main-nav">
    <a class="is-active" style="left:0">Home</a>
    <a style="left:95px">Magazine</a>
    <a style="left:197px">Calender</a>
    <a style="left:295px">Galleries</a>
    <a style="left:390px">Art</a>
    <a style="left:447px">Shop</a>
    <a style="left:519px">Artists</a>
    <a style="left:598px">Community</a>
    <a style="left:713px">Add</a>
  </nav>

  <h1 class="abs artist-name">Orin Haskel</h1>

  <nav class="profile-tabs">
    <a class="is-active" style="left:220px">Profile</a>
    <a style="left:308px">Artworks</a>
    <a style="left:396px">For Sale</a>
    <a style="left:484px">Network</a>
    <a style="left:572px">Reviews</a>
    <a style="left:660px">Comments</a>
  </nav>

  <section class="abs profile-panel"></section>

  <div class="abs feature-frame">
    <div class="feature-image" role="img" aria-label="Featured photograph: a passenger train passing along railway tracks"></div>
  </div>

  <div class="abs thumb-strip">
    <span class="thumb-arrow" style="left:0"><svg width="8" height="12" viewBox="0 0 8 12" aria-hidden="true"><polygon points="7,0 7,12 1,6" fill="#dcdcdc"/></svg></span>
    <span class="thumb" style="left:22px"><span role="img" aria-label="Thumbnail: portrait photograph" style="background:linear-gradient(#7e8a8c,#4a3a30)"></span></span>
    <span class="thumb" style="left:82px"><span role="img" aria-label="Thumbnail: portrait photograph" style="background:linear-gradient(#b8a08a,#3a2a24)"></span></span>
    <span class="thumb" style="left:142px"><span role="img" aria-label="Thumbnail: street photograph" style="background:linear-gradient(#6f7a5a,#b8b4a8)"></span></span>
    <span class="thumb" style="left:202px"><span role="img" aria-label="Thumbnail: train photograph" style="background:linear-gradient(#a8c0de,#8f8a84 50%,#7b6f64)"></span></span>
    <span class="thumb" style="left:262px"><span role="img" aria-label="Thumbnail: red building wall" style="background:linear-gradient(#8fb0d8,#b5452e 30%)"></span></span>
    <span class="thumb" style="left:322px"><span role="img" aria-label="Thumbnail: graffiti wall" style="background:linear-gradient(#c9a74a,#5a6a78)"></span></span>
    <span class="thumb-arrow" style="left:383px"><svg width="8" height="12" viewBox="0 0 8 12" aria-hidden="true"><polygon points="1,0 1,12 7,6" fill="#dcdcdc"/></svg></span>
  </div>

  <h2 class="abs buzz-title">News &amp; Buzz</h2>
  <p class="abs buzz-item" style="top:271px">Watchlist Artist: Delia Marsh</p>
  <p class="abs buzz-item" style="top:291px">Watchlist Artist: Teresa Quill</p>
  <p class="abs buzz-item" style="top:311px">Ansel Brook: On Our Worldwide Watchlist</p>

  <div class="abs panel-divider"></div>
  <div class="abs avatar" role="img" aria-label="Artist avatar image"></div>
  <p class="abs avatar-caption">Artist. Writer. Artlover.</p>

  <section class="abs quick-facts">
    <h2>QUICK FACTS</h2>
    <dl>
      <dt>BIRTHPLACE</dt><dd>Paris</dd>
      <dt>BIRTH YEAR</dt><dd>1974</dd>
      <dt>LIVES IN</dt><dd>Paris</dd>
      <dt>WORKS IN</dt><dd>Paris</dd>
    </dl>
  </section>

  <section class="abs statement">
    <h2>STATEMENT</h2>
    <p>Orin Haskel lives and works in and around Paris.&nbsp; His photography has been shown in all kinds of small galleries, clubs, and alternative arts spaces.&nbsp; He is particularly interested in creating a documentation of people in ordinary, everyday activities, looking for the moments of beauty or magic in the quotidien.</p>
  </section>

  <div class="abs share-row" aria-label="Share options">
    <span style="background:#3b5a9a"></span>
    <span style="background:#4fa8d8"></span>
    <span style="background:#2a72a8"></span>
    <span style="background:#2f6aa0"></span>
    <span style="background:#4a7fc0"></span>
    <span style="background:#3c9a3c"></span>
    <span style="background:#8aa8c8"></span>
    <span style="background:#4cb84c;border-radius:50%"></span>
    <span style="background:#e8b820"></span>
    <span style="background:#b8c8b0"></span>
  </div>

  <footer class="abs site-footer">
    <nav class="footer-links">
      <a style="left:416px">CONTACT</a>
      <a style="left:482px">ABOUT</a>
      <a style="left:531px">ADVERTISE</a>
      <a style="left:597px">TERMS</a>
      <a style="left:646px">JOIN THE TEAM</a>
      <a style="left:732px">FAQ</a>
    </nav>
    <p class="copyright">2012 © CanvoMira. All Rights Received.</p>
  </footer>

</body>
</html>
```